Road Sign at our office 84 in X 48 in - Small Billboard

Kestrel Electrical
Electrical & Lighting Services

- we need a sign design for our small business/company based in Calhoun, GA called Kestrel Electrical - "our mission is to provide Northwest Georgia with dependable, high-quality electrical services that prioritize safety, integrity, and long-term reliability. As a woman-owned business with over 25 years of experience, we are committed to delivering exceptional workmanship and personalized service for every commercial, residential, and industrial project we undertake. We stand behind our work with a lifetime warranty—because your trust is our most powerful connection."

display logo, phone number, and open to other ideas without being cluttered, maybe instead of full website address, just use @ksrelectrical and it will send them to all of our website and socials...

it needs to be easy to read as they drive down the road
this is a place where people may be traveling at high speeds, make sure it's easy to see and understand at a glance.
It will be hanging 20-24ft from the ground. Like a small billboard.

https://ksrelectricworks.com/

Industry/Entity Type

Electrical Contractor

Requirements
Nice to have
• match the look and feel of website and socials

```html
<!DOCTYPE html>
<html lang="en">
<head>
<meta charset="utf-8">
<title>Kestrel Electrical – Road Sign</title>
<link rel="stylesheet" href="https://fonts.googleapis.com/css2?family=Montserrat:wght@500;600;700&display=swap">
<style>
  :root {
    --page-bg: #eef0f2;
    --sign-dark: #140b06;
    --sign-warm: #3a2010;
    --brand-red: #e5332a;
    --brand-orange: #ea5a2b;
    --brand-yellow: #f6b816;
    --text-light: #ffffff;
    --flame-deep: #b8420f;
    --flame-light: #f39a2a;
  }
  * { box-sizing: border-box; margin: 0; padding: 0; }
  html, body {
    width: 1000px; height: 1200px; overflow: hidden;
    background: var(--page-bg);
    font-family: "Montserrat", Arial, sans-serif;
  }
  .sign {
    position: absolute; left: 21px; top: 326px;
    width: 958px; height: 548px; overflow: hidden;
    background: var(--sign-dark);
  }
  .sign__backdrop {
    position: absolute; inset: 0;
    background:
      radial-gradient(ellipse 60% 55% at 48% 45%, rgba(120,70,35,.55), transparent 70%),
      linear-gradient(180deg, #1a0f08 0%, var(--sign-warm) 55%, #1c110a 100%);
  }
  .sign__flame-art {
    position: absolute; right: 0; top: 135px; width: 170px; height: 413px;
    background: linear-gradient(200deg, transparent 10%, rgba(184,66,15,.35) 45%, rgba(243,154,42,.55) 100%);
  }
  .brand {
    position: absolute; left: 40px; top: 82px;
    display: flex; align-items: center; gap: 18px;
  }
  .brand__mark {
    width: 64px; height: 64px; border-radius: 50%;
    background: var(--brand-orange);
  }
  .brand__name {
    font-weight: 700; font-size: 46px; color: var(--text-light);
    letter-spacing: -0.5px; white-space: nowrap;
  }
  .tagline {
    position: absolute; left: 537px; top: 56px;
    display: flex; align-items: center; gap: 18px;
  }
  .tagline__icon { width: 70px; height: 70px; }
  .tagline__text {
    font-weight: 600; font-size: 24px; line-height: 1.2;
    color: var(--brand-orange); text-transform: uppercase;
  }
  .services {
    position: absolute; left: 0; top: 210px; width: 958px; height: 100px;
  }
  .service {
    position: absolute; top: 0; width: 240px; margin-left: -120px;
    display: flex; flex-direction: column; align-items: center; gap: 18px;
  }
  .service__badge {
    width: 58px; height: 58px; border-radius: 50%;
    display: flex; align-items: center; justify-content: center;
  }
  .service__badge--orange { background: var(--brand-orange); }
  .service__badge--yellow { background: var(--brand-yellow); }
  .service__badge svg { width: 32px; height: 32px; }
  .service__label {
    font-weight: 500; font-size: 17px; color: var(--text-light);
    text-transform: uppercase; white-space: nowrap;
  }
  .service--lighting { left: 143px; top: 4px; }
  .service--electrical { left: 390px; }
  .service--security { left: 638px; }
  .service--commercial { left: 855px; top: -4px; }
  .experience {
    position: absolute; left: 0; width: 958px; top: 340px;
    text-align: center; font-weight: 600; font-size: 42px; color: var(--text-light);
  }
  .handle {
    position: absolute; left: 0; width: 958px; top: 392px;
    text-align: center; font-weight: 600; font-size: 40px; color: var(--brand-red);
  }
  .phone-band {
    position: absolute; left: 0; bottom: 0; width: 958px; height: 98px;
    background: var(--brand-red);
    display: flex; align-items: center; justify-content: center; gap: 26px;
  }
  .phone-band__icon { width: 56px; height: 56px; }
  .phone-band__number {
    font-weight: 700; font-size: 82px; color: var(--text-light); letter-spacing: 1px;
  }
</style>
</head>
<body>
  <main class="sign">
    <div class="sign__backdrop" role="img" aria-label="Dimly lit living room and kitchen interior with warm lamp light"></div>
    <div class="sign__flame-art" role="img" aria-label="Faint flame-coloured bird decoration along the right edge"></div>

    <div class="brand">
      <span class="brand__mark"></span>
      <span class="brand__name">Kestrel Electrical</span>
    </div>

    <div class="tagline">
      <svg class="tagline__icon" viewBox="0 0 70 70" fill="none" stroke="#ea5a2b" stroke-width="2.5" stroke-linecap="round" stroke-linejoin="round">
        <circle cx="35" cy="35" r="32"/>
        <line x1="29" y1="14" x2="29" y2="22"/>
        <line x1="41" y1="14" x2="41" y2="22"/>
        <path d="M22 22h26v10a13 13 0 0 1-26 0z"/>
        <path d="M36 26l-4 7h6l-4 7"/>
        <path d="M35 45v8c0 6-8 6-12 10"/>
        <circle cx="8" cy="55" r="3"/>
      </svg>
      <div class="tagline__text">Comprehensive<br>Electrical Services</div>
    </div>

    <section class="services">
      <div class="service service--lighting">
        <span class="service__badge service__badge--orange">
          <svg viewBox="0 0 32 32" fill="none" stroke="#fff" stroke-width="2" stroke-linecap="round">
            <path d="M11 18a7 7 0 1 1 10 0c-1 1-2 2-2 4h-6c0-2-1-3-2-4z"/>
            <line x1="13" y1="25" x2="19" y2="25"/><line x1="14" y1="28" x2="18" y2="28"/>
            <line x1="16" y1="2" x2="16" y2="4"/><line x1="5" y1="7" x2="7" y2="8"/><line x1="27" y1="7" x2="25" y2="8"/>
          </svg>
        </span>
        <span class="service__label">Lighting Services</span>
      </div>
      <div class="service service--electrical">
        <span class="service__badge service__badge--yellow">
          <svg viewBox="0 0 32 32" fill="none" stroke="#fff" stroke-width="2" stroke-linecap="round" stroke-linejoin="round">
            <line x1="12" y1="4" x2="12" y2="10"/><line x1="20" y1="4" x2="20" y2="10"/>
            <path d="M8 10h16v6a8 8 0 0 1-16 0z"/>
            <path d="M17 13l-3 5h4l-3 5"/>
            <line x1="16" y1="24" x2="16" y2="29"/>
          </svg>
        </span>
        <span class="service__label">Electrical Services</span>
      </div>
      <div class="service service--security">
        <span class="service__badge service__badge--yellow">
          <svg viewBox="0 0 32 32" fill="none" stroke="#fff" stroke-width="2" stroke-linecap="round" stroke-linejoin="round">
            <path d="M4 15L16 5l12 10"/>
            <path d="M7 13v13h18V13"/>
            <rect x="11" y="16" width="10" height="6" rx="1"/>
            <path d="M16 17.5l-1.5 2h3l-1.5 2"/>
          </svg>
        </span>
        <span class="service__label">Electrical Segurity</span>
      </div>
      <div class="service service--commercial">
        <span class="service__badge service__badge--orange">
          <svg viewBox="0 0 32 32" fill="none" stroke="#fff" stroke-width="2" stroke-linecap="round">
            <path d="M11 18a7 7 0 1 1 10 0c-1 1-2 2-2 4h-6c0-2-1-3-2-4z"/>
            <line x1="13" y1="25" x2="19" y2="25"/><line x1="14" y1="28" x2="18" y2="28"/>
            <line x1="16" y1="9" x2="16" y2="17"/><path d="M18 10.5h-3a1.5 1.5 0 0 0 0 3h2a1.5 1.5 0 0 1 0 3h-3"/>
          </svg>
        </span>
        <span class="service__label">Commercial</span>
      </div>
    </section>

    <p class="experience">over 25 years of experience</p>
    <p class="handle">@ksrelectrical</p>

    <div class="phone-band">
      <svg class="phone-band__icon" viewBox="0 0 24 24" fill="#ffffff">
        <path d="M6.6 10.8a15.1 15.1 0 0 0 6.6 6.6l2.2-2.2a1 1 0 0 1 1-.25 11.4 11.4 0 0 0 3.6.57 1 1 0 0 1 1 1V20a1 1 0 0 1-1 1A17 17 0 0 1 3 4a1 1 0 0 1 1-1h3.5a1 1 0 0 1 1 1c0 1.25.2 2.45.57 3.6a1 1 0 0 1-.25 1z"/>
      </svg>
      <span class="phone-band__number">706-555-0148</span>
    </div>
  </main>
</body>
</html>
```